Business Card Design for Retail Product Line

We need a two-sided, full-color business card for a new oral care product line. The feel of the card should invoke emotions of happiness and health. It should be bright, cheerful and modern in appearance. The card should be mostly matte finish, but with elements of spot-gloss and/or raised/embossed features (print, logo, tag lines, etc.).

Target Market(s)

People who are into whole-body health, eat well and understand the importance of nutrition.

Industry/Entity Type

Health And Wellness

Contact Information for Business Card

The logo, color scheme and tag-lines have all been developed and artwork is attached. Card is to be standard-sized and should use a mix of clean, sans-serif fonts; the main font (DIN) is attached as well. The card will be used for 3 individuals and should include placeholders for:
1. Name
2. Title (for example, "CEO")
3. Business address
4. Phone number
5. Website
6. Email address

Font styles to use
Sans Serif
Other font styles liked:
• DIN font

Colors
faa54b
000000
5c5c5c
a2ce44

Requirements
Must have
• 2 sides
• Full color orange on one side
• Image of DNA leaves
• Tag line "Smile from the Inside Out", on single side with orange background
• Company Logo (Brelu) on same side as text (name, phone, address, etc.)
• Name, Title, Business Address, Phone Number, Website, Email address
• UPDATE: "Sunny Crest", not "Sunn Y Crest"
Should not have
• Calligraphy
• Dark colors
• UPDATE!! Do not include "Turmeric infused toothpaste" on the business card
• UPDATE #2!! Do not include "Sunny Crest" on the business card

```html
<!DOCTYPE html>
<html lang="en">
<head>
<meta charset="utf-8">
<title>Brelu Business Card</title>
<link href="https://fonts.googleapis.com/css2?family=Barlow:wght@400;500;600;700&family=Barlow+Semi+Condensed:wght@600&display=swap" rel="stylesheet">
<style>
  :root {
    --backdrop: #ece8e1;
    --orange: #faa54b;
    --orange-deep: #e8962f;
    --sun: #f2cd3d;
    --white: #ffffff;
    --ink: #000000;
    --grey: #5c5c5c;
    --grey-text: #444444;
    --green: #a2ce44;
    --green-label: #8cc63f;
    --leaf-dark: #2e9e48;
    --leaf-light: #9bd04a;
  }
  html, body {
    margin: 0;
    padding: 0;
    width: 1200px;
    height: 1076px;
    overflow: hidden;
    background: var(--backdrop);
  }
  .sheet {
    width: 1200px;
    height: 1076px;
    display: flex;
    flex-direction: column;
    align-items: center;
    justify-content: center;
    gap: 30px;
  }
  .card {
    position: relative;
    width: 880px;
    height: 503px;
    overflow: hidden;
    box-shadow: 0 6px 18px rgba(0,0,0,0.18);
  }

  /* Front side */
  .card-front {
    background: linear-gradient(160deg, var(--orange-deep) 0%, var(--sun) 40%, var(--sun) 60%, var(--orange-deep) 100%);
  }
  .tagline {
    position: absolute;
    left: 300px;
    top: 140px;
    margin: 0;
    color: var(--white);
  }
  .tagline-lead {
    display: block;
    font-family: "Barlow", sans-serif;
    font-weight: 700;
    font-size: 118px;
    line-height: 0.9;
    letter-spacing: -1px;
  }
  .tagline-rest {
    display: block;
    font-family: "Barlow Semi Condensed", sans-serif;
    font-weight: 600;
    font-size: 66px;
    line-height: 0.95;
    text-transform: uppercase;
    margin-top: 6px;
  }

  /* Back side */
  .card-back {
    background: var(--white);
  }
  .dna-leaves {
    position: absolute;
    left: 55px;
    top: 30px;
    width: 335px;
    height: 473px;
    border-radius: 160px 160px 40px 40px;
    background: linear-gradient(170deg, var(--leaf-light) 0%, var(--leaf-dark) 55%, #c9c9c9 100%);
  }
  .brand {
    position: absolute;
    left: 470px;
    top: 62px;
    display: flex;
    align-items: center;
    gap: 16px;
  }
  .brand-dot {
    width: 26px;
    height: 26px;
    border-radius: 50%;
    background: var(--green);
  }
  .brand-name {
    font-family: "Barlow", sans-serif;
    font-weight: 600;
    font-size: 110px;
    line-height: 1;
    color: var(--grey);
  }
  .contact {
    position: absolute;
    left: 470px;
    top: 262px;
    font-family: "Barlow", sans-serif;
    color: var(--grey-text);
  }
  .contact-name {
    margin: 0;
    font-size: 32px;
    font-weight: 600;
    line-height: 1.05;
  }
  .contact-title {
    margin: 0 0 10px;
    font-size: 21px;
    font-weight: 500;
    line-height: 1.2;
    color: var(--green-label);
  }
  .contact-address {
    margin: 0 0 6px;
    font-style: normal;
    font-size: 22px;
    line-height: 1.3;
  }
  .contact-lines {
    margin: 0;
    padding: 0;
    list-style: none;
    font-size: 21px;
    line-height: 1.25;
  }
  .contact-label {
    color: var(--green-label);
    font-weight: 600;
  }
</style>
</head>
<body>
<main class="sheet">
  <section class="card card-front" aria-label="Card front">
    <p class="tagline">
      <span class="tagline-lead">shine</span>
      <span class="tagline-rest">From within<br>every day</span>
    </p>
  </section>

  <section class="card card-back" aria-label="Card back">
    <div class="dna-leaves" role="img" aria-label="Illustration of a DNA helix growing into green leaves"></div>
    <div class="brand">
      <span class="brand-name">Brelu</span>
      <span class="brand-dot" aria-hidden="true"></span>
    </div>
    <div class="contact">
      <h1 class="contact-name">Alex Morgan</h1>
      <p class="contact-title">CEO</p>
      <address class="contact-address">Your Address, 2nd Ste<br>Fairview, Texas 1234, USA</address>
      <ul class="contact-lines">
        <li><span class="contact-label">Phone:</span> (555).555.0123</li>
        <li><span class="contact-label">Email:</span> hello@brelumail.com</li>
        <li><span class="contact-label">Web:</span> www.breluweb.com</li>
      </ul>
    </div>
  </section>
</main>
</body>
</html>
```